Quorvex clinic business card - double sided for young clinic

I require business cards for my aesthetic clinic specialising in the below treatments. I would like the cards to be modern as my clinic base are young 22-35 years old. I require my logo on it and would like the edges to be rounded.

I have an aesthetic clinic specialising in :
Quorvex
Lip Enhancement
Chemical Peels
Facial Fillers
Non Surgical Face Lift

I would the cards to have the following information on them:
My logo - (in grey/silver)
address
Phone number
services

Colours :
White/grey/silver and red

a nice image on there, perhaps a set of lips as this is a main service i deliver

Company Name: PDA Address: 52 Farrowmere Road, 4 Brackwell High Street, KT9 4WQ Phone: 0208 794 2160 Website: www.penningtondoweaesthetics.co.uk

Target Market(s)

clinics 22-45 years old mainly female

Industry/Entity Type

Business

Contact Information for Business Card

as above

Requirements
Must have
• logo
• Address
• Email
• Phone number
• Services i offer
Nice to have
• images

```html
<!DOCTYPE html>
<html lang="en">
<head>
<meta charset="utf-8">
<title>PDA Business Card</title>
<link rel="stylesheet" href="https://fonts.googleapis.com/css2?family=Noto+Serif:wght@400;700&display=swap">
<style>
  :root {
    --page-bg: #ffffff;
    --silver-edge: #bba9aa;
    --silver-mid: #e4dcdc;
    --silver-light: #ffffff;
    --ink: #231f20;
    --red: #ee3a3d;
    --red-faint: #f25a5c;
    --white: #ffffff;
    --skin: #fcdcb4;
  }
  * { margin: 0; padding: 0; box-sizing: border-box; }
  html, body { width: 1200px; height: 1000px; overflow: hidden; background: var(--page-bg); }
  body { position: relative; font-family: "Noto Serif", Georgia, serif; }

  .card {
    position: absolute;
    width: 630px;
    height: 361px;
    border-radius: 40px;
    box-shadow: 0 1px 4px rgba(0,0,0,0.3);
    overflow: hidden;
  }
  .card-front {
    left: 150px; top: 117px;
    background: linear-gradient(90deg, var(--silver-edge) 0%, var(--silver-mid) 25%, var(--silver-light) 50%, var(--silver-mid) 75%, var(--silver-edge) 100%);
  }
  .brand-dot {
    position: absolute;
    left: 255px; top: 90px;
    width: 120px; height: 120px;
    border-radius: 50%;
    background: var(--ink);
  }
  .brand-name {
    position: absolute;
    left: 0; right: 0; top: 224px;
    text-align: center;
    color: var(--ink);
    font-weight: 400;
    font-size: 26px;
    line-height: 30px;
    letter-spacing: 3px;
    text-transform: uppercase;
  }

  .card-back { left: 420px; top: 521px; background: var(--red); }
  .mask-art {
    position: absolute;
    left: 40px; top: 45px;
    width: 235px; height: 145px;
    border-radius: 20px 20px 60px 60px;
    background: var(--skin);
    box-shadow: 6px 10px 18px rgba(120,0,0,0.35);
  }
  .faint-mark { position: absolute; left: 175px; top: 135px; width: 160px; height: 160px; border-radius: 50%; background: var(--red-faint); opacity: 0.45; }
  .faint-name { position: absolute; left: 175px; top: 190px; width: 160px; text-align: center; color: var(--red); font-size: 36px; opacity: 0.6; }
  .cross { position: absolute; left: 57px; top: 250px; }

  .services { position: absolute; left: 313px; top: 45px; list-style: none; }
  .services li {
    color: var(--white);
    font-size: 19px;
    line-height: 25px;
    text-shadow: 1px 1px 2px rgba(0,0,0,0.45);
    display: flex; align-items: center; gap: 6px;
  }
  .contact {
    position: absolute; right: 25px;
    color: var(--white);
    font-size: 18px;
    line-height: 25px;
    text-align: right;
    text-shadow: 1px 1px 2px rgba(0,0,0,0.3);
  }
  .address { top: 190px; }
  .address-label { display: flex; justify-content: flex-end; align-items: center; gap: 12px; }
  .phone, .web { display: flex; justify-content: flex-end; align-items: center; gap: 12px; }
  .phone { top: 284px; }
  .web { top: 314px; right: 22px; }
</style>
</head>
<body>

<section class="card card-front">
  <div class="brand-dot"></div>
  <p class="brand-name">Pennington Dowe<br>Aesthetics</p>
</section>

<section class="card card-back">
  <div class="faint-mark"></div>
  <div class="faint-name">PDA</div>
  <div class="mask-art" role="img" aria-label="Illustration of two pale theatre-style masks, one with red lips"></div>

  <svg class="cross" width="66" height="66" viewBox="0 0 66 66">
    <path d="M22 0h22v22h22v22H44v22H22V44H0V22h22z" fill="#ffffff" opacity="0.12"/>
  </svg>

  <ul class="services">
    <li><svg width="30" height="16" viewBox="0 0 30 16"><path d="M2 8l7 6L28 1" fill="none" stroke="#fff" stroke-width="3"/></svg>Quorvex</li>
    <li><svg width="30" height="16" viewBox="0 0 30 16"><path d="M2 8l7 6L28 1" fill="none" stroke="#fff" stroke-width="3"/></svg>Lip Enhancement</li>
    <li><svg width="30" height="16" viewBox="0 0 30 16"><path d="M2 8l7 6L28 1" fill="none" stroke="#fff" stroke-width="3"/></svg>Chemical Peels</li>
    <li><svg width="30" height="16" viewBox="0 0 30 16"><path d="M2 8l7 6L28 1" fill="none" stroke="#fff" stroke-width="3"/></svg>Facial Fillers</li>
    <li><svg width="30" height="16" viewBox="0 0 30 16"><path d="M2 8l7 6L28 1" fill="none" stroke="#fff" stroke-width="3"/></svg>Non Surgical Face Lift</li>
  </ul>

  <div class="contact address">
    <div class="address-label">
      <svg width="26" height="24" viewBox="0 0 26 24"><path d="M13 1L1 12h4v11h16V12h4z" fill="#fff"/><rect x="8" y="14" width="4" height="4" fill="#ee3a3d"/><rect x="14" y="14" width="4" height="4" fill="#ee3a3d"/></svg>
      <span>Address:</span>
    </div>
    <p>52 Farrowmere Road, 4 Brackwell</p>
    <p>High Street, KT9 4WQ</p>
  </div>

  <div class="contact phone">
    <span>0208 794 2160</span>
    <svg width="28" height="28" viewBox="0 0 28 28"><rect x="1" y="1" width="26" height="26" rx="7" fill="#fff"/><path d="M10 7c-2 1-2 4 0 8s5 6 7 6l1-3-3-2-1 1c-1-1-3-3-3-5l1-1-1-3z" fill="#999"/></svg>
  </div>

  <div class="contact web">
    <span>www.penningtondoweaesthetics.co.uk</span>
    <svg width="34" height="28" viewBox="0 0 34 28"><circle cx="12" cy="12" r="10" fill="none" stroke="#fff" stroke-width="2"/><path d="M2 12h20M12 2v20M5 6h14M5 18h14" stroke="#fff" stroke-width="1.5"/><circle cx="22" cy="17" r="5" fill="#ee3a3d" stroke="#fff" stroke-width="2"/><path d="M26 21l6 6" stroke="#fff" stroke-width="3"/></svg>
  </div>
</section>

</body>
</html>
```